Album cover for modern electronic pop music - sci-fi

Check out my website www.tamostby-music.example - the album should reflect this website.

Use the picture of my face on the cover - The second photo is a collage which you can use (only) as inspiration. And there is a picture with different fonts I like.

Must have my face, the name "Tam Ostby" and the album title "Waiting Past Midnight, Still. Feel free to minimise my face and play around with that.

Ideas (for inspiration):
1. A drawn movie poster like from a sci-fi movie from the eighties (but modern font).
2. Hints of stars, a sunset and the big city (very subtle).
3. Font - see image enclosed.

The album cover is for electronic pop music (you can listen to it on my website).
Updates

The Brief is updated - check it out. Added Sunday, December 11, 2016

Information updated - a new picture with fonts I like has been added. Added Monday, December 12, 2016

Industry/Entity Type

Electronic

Requirements
Must have
• My face. The name "Tam Ostby" and the Album title "Waiting Past Midnight, Still".
• Look at www.tamostby-music.example, the cover should reflect this website.
• It will be mostly seen in a small format (Plinkwave, Tunemarsh, Vespo), so make sure it looks good minimised.
Should not have
• There should not be to much information. Needs to be simple and clean.

```html
<!DOCTYPE html>
<html lang="en">
<head>
<meta charset="utf-8">
<title>Tam Ostby – Waiting Past Midnight, Still</title>
<link rel="stylesheet" href="https://fonts.googleapis.com/css2?family=Josefin+Sans:wght@300;400&display=swap">
<style>
  :root {
    --night: #000000;
    --deep-green: #0f2a10;
    --neon-green: #2f6b2a;
    --neon-red: #e2364f;
    --title-red: #ff5f70;
    --subtitle-white: #f2f2f2;
  }
  html, body {
    margin: 0;
    padding: 0;
    width: 1200px;
    height: 1200px;
    overflow: hidden;
    background: var(--night);
  }
  .cover {
    position: relative;
    width: 1200px;
    height: 1200px;
    background: var(--night);
    overflow: hidden;
  }
  .portrait {
    position: absolute;
    left: 0;
    top: 0;
    width: 1200px;
    height: 1200px;
  }
  .artist-name {
    position: absolute;
    left: 0;
    right: 0;
    top: 1000px;
    margin: 0;
    text-align: center;
    font-family: "Josefin Sans", sans-serif;
    font-weight: 300;
    font-size: 84px;
    letter-spacing: 0.32em;
    padding-left: 0.32em;
    line-height: 1;
    color: var(--title-red);
    text-shadow: 0 0 10px rgba(255, 60, 80, 0.45);
  }
  .album-title {
    position: absolute;
    left: 0;
    right: 0;
    top: 1094px;
    margin: 0;
    text-align: center;
    font-family: "Josefin Sans", sans-serif;
    font-weight: 400;
    font-size: 34px;
    letter-spacing: 0.14em;
    padding-left: 0.14em;
    line-height: 1;
    text-transform: uppercase;
    color: var(--subtitle-white);
  }
</style>
</head>
<body>
  <main class="cover">
    <svg class="portrait" viewBox="0 0 1200 1200" role="img" aria-label="Portrait photo of the artist at night on a dark city street, face lit in neon green with red edge light">
      <defs>
        <radialGradient id="portrait-glow" cx="600" cy="470" r="520" gradientUnits="userSpaceOnUse">
          <stop offset="0" stop-color="var(--neon-green)"/>
          <stop offset="0.35" stop-color="var(--deep-green)"/>
          <stop offset="0.55" stop-color="#1a0b0d"/>
          <stop offset="1" stop-color="var(--night)" stop-opacity="0"/>
        </radialGradient>
        <linearGradient id="street-haze" x1="0" y1="0" x2="0" y2="1">
          <stop offset="0" stop-color="#000"/>
          <stop offset="0.55" stop-color="#0c110c"/>
          <stop offset="1" stop-color="#000"/>
        </linearGradient>
        <radialGradient id="rim-light" cx="600" cy="470" r="300" gradientUnits="userSpaceOnUse">
          <stop offset="0.6" stop-color="var(--neon-red)" stop-opacity="0"/>
          <stop offset="0.85" stop-color="var(--neon-red)" stop-opacity="0.35"/>
          <stop offset="1" stop-color="var(--neon-red)" stop-opacity="0"/>
        </radialGradient>
      </defs>
      <rect x="0" y="120" width="1200" height="780" fill="url(#street-haze)"/>
      <rect x="0" y="0" width="1200" height="1000" fill="url(#portrait-glow)"/>
      <ellipse cx="600" cy="470" rx="300" ry="340" fill="url(#rim-light)"/>
    </svg>

    <h1 class="artist-name">TAM OSTBY</h1>
    <p class="album-title">Waiting Past Midnight, Still</p>
  </main>
</body>
</html>
```